Electronic Music Artist needs an Album Cover

DRELL is an electronic musician from Boston, Massachusetts. He needs an album cover that captures the essence of his music. The album is called Waypoints, which represents his experiences growing up, positive and negative. He would like to see designs that involves color and creativity. Attached are some examples of artworks that DRELL likes. He also included a few of his original photos (optional to use. Using a photo will not effect his final decision!), and his logo.
Updates

Colors

Designer to choose colors to be used in the design.

Requirements
Must have
• My project must have the text "Waypoints" and "DRELL", and the logo (attached in the files). The logo should not be the main subject of the artwork. Everything must look aesthetically pleasing.
Nice to have
• It would be nice to have some sort of creative graphic design (see example album covers for reference). Also, in one of the references, there is a column on the left hand side with some text in it. That could be cool to include, but without the asian text.
Should not have
• The project should not have any other language besides English.

```html
<!DOCTYPE html>
<html lang="en">
<head>
<meta charset="utf-8">
<title>DRELL — Waypoints</title>
<link rel="stylesheet" href="https://fonts.googleapis.com/css2?family=Permanent+Marker&family=Kaushan+Script&display=swap">
<style>
  :root {
    --stage: #2a2a2c;
    --cover-black: #050507;
    --sky-blue: #5fc6ea;
    --sky-pale: #e9f3f4;
    --dusk-amber: #e0a46a;
    --violet: #4a3f9c;
    --magenta: #e0378f;
    --neon-red: #e3263f;
    --deep-red: #7b1426;
    --title-ice: #d6f1f3;
  }
  html, body {
    margin: 0;
    padding: 0;
    width: 1200px;
    height: 1015px;
    overflow: hidden;
    background: var(--stage);
  }
  .canvas {
    position: relative;
    width: 1200px;
    height: 1015px;
  }
  .album-cover {
    position: absolute;
    left: 170px;
    top: 47px;
    width: 860px;
    height: 860px;
    background: var(--cover-black);
    overflow: hidden;
  }
  .album-cover svg { display: block; }
  .title-block {
    position: absolute;
    left: 250px;
    top: 300px;
    transform: rotate(11deg);
    transform-origin: left top;
    color: var(--title-ice);
    line-height: 1;
  }
  .artist-name {
    display: block;
    margin-left: 80px;
    font-family: "Permanent Marker", cursive;
    font-size: 96px;
    letter-spacing: 8px;
  }
  .album-title {
    display: block;
    margin-top: -18px;
    font-family: "Kaushan Script", cursive;
    font-size: 118px;
  }
  .label-mark {
    position: absolute;
    right: 36px;
    bottom: 30px;
    font-family: "Permanent Marker", cursive;
    font-size: 30px;
    color: var(--title-ice);
    letter-spacing: 2px;
  }
</style>
</head>
<body>
<div class="canvas">
  <section class="album-cover">
    <svg width="860" height="860" viewBox="0 0 860 860" role="img" aria-label="Night-city photograph: a lit tower seen through a window grid, with neon pink and red light columns, cut into diagonal slices">
      <defs>
        <linearGradient id="sky-slice" x1="0" y1="0" x2="0.4" y2="1">
          <stop offset="0" stop-color="var(--sky-blue)"/>
          <stop offset="0.35" stop-color="var(--sky-pale)"/>
          <stop offset="0.75" stop-color="var(--dusk-amber)"/>
          <stop offset="1" stop-color="#2b1c1a"/>
        </linearGradient>
        <linearGradient id="pink-column" x1="0" y1="0" x2="0" y2="1">
          <stop offset="0" stop-color="var(--sky-pale)"/>
          <stop offset="0.3" stop-color="var(--violet)"/>
          <stop offset="0.65" stop-color="var(--magenta)"/>
          <stop offset="1" stop-color="#3a1030"/>
        </linearGradient>
        <linearGradient id="red-column" x1="0" y1="0" x2="0" y2="1">
          <stop offset="0" stop-color="var(--sky-blue)"/>
          <stop offset="0.3" stop-color="var(--violet)"/>
          <stop offset="0.7" stop-color="var(--neon-red)"/>
          <stop offset="1" stop-color="var(--deep-red)"/>
        </linearGradient>
      </defs>
      <rect width="860" height="860" fill="var(--cover-black)"/>
      <polygon class="photo-slice sky" points="0,0 470,0 40,820 0,820" fill="url(#sky-slice)"/>
      <polygon class="photo-slice pink" points="560,60 680,40 500,860 200,860" fill="url(#pink-column)"/>
      <polygon class="photo-slice red" points="720,40 860,20 860,860 560,860" fill="url(#red-column)"/>
      <polygon class="photo-slice violet" points="640,0 860,0 860,60 700,90" fill="var(--violet)" opacity="0.8"/>
    </svg>
    <div class="title-block">
      <span class="artist-name">DRELL</span>
      <span class="album-title">Waypoints</span>
    </div>
    <div class="label-mark">DRX</div>
  </section>
</div>
</body>
</html>
```